Poster for a Bicycle show/Expo

We need a poster for a Bicycle show/Expo and sustainable transport. Exhibitors will sell bikes, cycling clothing, accessories, etc. ...
This show is annual and the Poster is for the 2016 edition.

Your concept must be compatible in a landscape format. (We will ourselves adaptations of different formats.)
Width: 210 mm
Height: 297 mm
It's necessary for us to have the source file (vector) for make, later, the different format (flyers, website, ...)

Content of the Poster:
- 1 big picture (one of the two attached)
- Big title (typo-title worked): « Foire du Rouet » (« Salon » or « Salon du » can be small and « Vélo » big.)
- Subtitle: « et de la mobilité durable »
- Date: « 18, 19 et 20 mars 2016 » or « 18-20 mars 2016 »
- Place: « Halle RTP - Gare de Plantaz »
- Text line 1: « www.foire-du-rouet.ch »
- Text line 2: « Entrée gratuite »
- Text line 3: « Ve 18 mars de 17h à 20h - Sa 19 mars de 10h à 18h - Di 20 mars de 10h à 17h »
- Please, leave a zone in the poster for sponsors logos
(The predominant information (most visible) are: « Vélo » and « 18, 19 et 20 mars 2016 » or « 18-20 mars 2016 »)

Target Market(s)

Bicycle fan

Industry/Entity Type

Sporting Good

Font styles to use
Serif
Sans Serif

Colors
add136
ffffff
ec1f27

Requirements
Must have
• The style must be modern, dynamic, bright colors.

```html
<!DOCTYPE html>
<html lang="fr">
<head>
<meta charset="utf-8">
<title>Foire du Rouet 2016</title>
<link rel="stylesheet" href="https://fonts.googleapis.com/css2?family=Montserrat:wght@200;300;400;500;600;700&display=swap">
<style>
  :root {
    --sky-top: #2f86d6;
    --sky-mid: #7fbcec;
    --sky-low: #c9e3f7;
    --white: #ffffff;
    --red: #ec1f27;
    --green: #add136;
    --ink: #1b1b1b;
    --panel: rgba(12, 12, 14, 0.9);
    --band: rgba(255, 255, 255, 0.72);
  }
  * { box-sizing: border-box; margin: 0; padding: 0; }
  html, body { width: 849px; height: 1200px; overflow: hidden; background: var(--white); }
  .poster {
    position: relative; width: 849px; height: 1200px; overflow: hidden;
    font-family: "Montserrat", sans-serif; color: var(--ink);
  }
  .sky-photo {
    position: absolute; inset: 0;
    background:
      radial-gradient(ellipse 45% 9% at 30% 62%, rgba(255,255,255,0.5), transparent 70%),
      radial-gradient(ellipse 55% 10% at 55% 90%, rgba(255,255,255,0.5), transparent 70%),
      linear-gradient(180deg, var(--sky-top) 0%, var(--sky-mid) 40%, var(--sky-low) 62%, var(--sky-mid) 80%, var(--sky-top) 100%);
  }
  .bike-clouds {
    position: absolute; left: 150px; top: 20px; width: 580px; height: 370px;
    background: radial-gradient(ellipse 50% 48% at 50% 52%, rgba(255,255,255,0.85), rgba(255,255,255,0.35) 60%, transparent 78%);
  }
  .tyre-tracks {
    position: absolute; left: 0; top: 300px; width: 849px; height: 90px;
    background: linear-gradient(180deg, transparent, rgba(255,255,255,0.45) 50%, transparent);
  }
  .title-band {
    position: absolute; left: 0; top: 440px; width: 849px; height: 290px;
    background: linear-gradient(180deg, transparent 0%, var(--band) 22%, var(--band) 78%, transparent 100%);
  }
  .globe {
    position: absolute; left: 368px; top: 480px; width: 240px; height: 230px; border-radius: 50%;
    background: radial-gradient(circle at 40% 40%, #9ccbe9, #3f7fb0 60%, #6fa06a 90%);
    opacity: 0.75;
  }
  .title { position: absolute; left: 0; top: 505px; width: 849px; text-align: center; }
  .title-small {
    display: block; font-weight: 200; font-size: 52px; letter-spacing: 2px; line-height: 1;
  }
  .title-big {
    display: block; margin-top: 2px; font-weight: 500; font-size: 120px; letter-spacing: 4px; line-height: 1;
  }
  .subtitle {
    position: absolute; top: 680px; left: 311px; width: 515px; height: 34px;
    background: var(--red); color: var(--white); border-radius: 17px 0 0 17px;
    font-weight: 600; font-size: 21px; line-height: 34px; text-align: center;
  }
  .info-panel {
    position: absolute; left: 170px; top: 860px; width: 509px; height: 252px;
    background: var(--panel); color: var(--white);
    border-radius: 26px 26px 0 0; text-align: center;
  }
  .info-icons {
    position: absolute; top: -34px; left: 0; width: 100%;
    display: flex; justify-content: center; gap: 48px;
  }
  .info-icons svg { width: 46px; height: 46px; }
  .info-date { margin-top: 44px; font-size: 18px; font-weight: 300; line-height: 22px; }
  .info-place { font-size: 18px; font-weight: 300; line-height: 22px; }
  .info-free { font-size: 19px; font-weight: 600; line-height: 24px; }
  .info-hours { margin-top: 14px; font-size: 21px; font-weight: 700; line-height: 34px; }
  .info-web { margin-top: 10px; font-size: 19px; font-weight: 700; }
  .sponsors {
    position: absolute; left: 0; top: 1125px; width: 849px; height: 75px;
    background: var(--white);
    display: flex; align-items: center; justify-content: space-around; padding: 0 14px;
  }
  .sponsor { font-size: 13px; font-weight: 600; color: var(--ink); display: flex; align-items: center; gap: 6px; }
  .sponsor-dot { width: 10px; height: 10px; border-radius: 50%; background: var(--green); }
  .sponsor-badge { width: 44px; height: 24px; background: var(--ink); }
</style>
</head>
<body>
<main class="poster">
  <div class="sky-photo" role="img" aria-label="Ciel bleu nuageux avec traces de pneus"></div>
  <div class="bike-clouds" role="img" aria-label="Vélo dessiné par des nuages dans le ciel"></div>
  <div class="tyre-tracks" role="img" aria-label="Traces de pneus blanches traversant le ciel"></div>

  <div class="title-band"></div>
  <div class="globe" role="img" aria-label="Globe terrestre derrière le titre"></div>
  <h1 class="title">
    <span class="title-small">Foire du</span>
    <span class="title-big">ROUET</span>
  </h1>
  <p class="subtitle">et de la mobilité durable</p>

  <section class="info-panel">
    <div class="info-icons">
      <svg viewBox="0 0 56 56" aria-hidden="true"><circle cx="28" cy="28" r="26" fill="#1b1b1b" stroke="#fff" stroke-width="2"/><rect x="16" y="18" width="24" height="21" rx="2" fill="none" stroke="#fff" stroke-width="2.5"/><line x1="16" y1="25" x2="40" y2="25" stroke="#fff" stroke-width="2.5"/><line x1="22" y1="15" x2="22" y2="20" stroke="#fff" stroke-width="2.5"/><line x1="34" y1="15" x2="34" y2="20" stroke="#fff" stroke-width="2.5"/></svg>
      <svg viewBox="0 0 56 56" aria-hidden="true"><circle cx="28" cy="28" r="26" fill="#1b1b1b" stroke="#fff" stroke-width="2"/><path d="M28 42 C20 32 19 28 19 25 a9 9 0 0 1 18 0 c0 3-1 7-9 17z" fill="#fff"/><circle cx="28" cy="25" r="3.5" fill="#1b1b1b"/></svg>
      <svg viewBox="0 0 56 56" aria-hidden="true"><circle cx="28" cy="28" r="26" fill="#1b1b1b" stroke="#fff" stroke-width="2"/><circle cx="28" cy="28" r="12" fill="none" stroke="#fff" stroke-width="2.5"/><path d="M28 21 V28 L33 31" fill="none" stroke="#fff" stroke-width="2.5"/></svg>
      <svg viewBox="0 0 56 56" aria-hidden="true"><circle cx="28" cy="28" r="26" fill="#1b1b1b" stroke="#fff" stroke-width="2"/><path d="M17 29 L25 37 L40 20" fill="none" stroke="#fff" stroke-width="3"/></svg>
    </div>
    <p class="info-date">18-20 Mars 2016</p>
    <p class="info-place">Halle RTP - Gare de Plantaz</p>
    <p class="info-free">Entrée gratuite</p>
    <p class="info-hours">Ve 18 Mars de 17h à 20h - Sa 19 Mars de<br>10h à 18h - Di 20 Mars de 10h à 17h</p>
    <p class="info-web">www.foire-du-rouet.ch</p>
  </section>

  <footer class="sponsors">
    <span class="sponsor"><span class="sponsor-dot"></span>Horizon Vert</span>
    <span class="sponsor">Cycle Avenir</span>
    <span class="sponsor">Nuagerie</span>
    <span class="sponsor">Vélocia</span>
    <span class="sponsor">Brunet Atelier</span>
    <span class="sponsor-badge"></span>
    <span class="sponsor">Sobriété 22</span>
  </footer>
</main>
</body>
</html>
```